Stationery Design Project - KORVELT-NINE

Presentation Folder
Size: A4
Notepad
Size: 250mm x 140mm
With Compliments Slip
Size: DL
210mm x 99mm
Letterhead
Size: A4 - 210mm x 297mm
Business Cards
Size: 90mm x 55mm

Company is called "KORVELT-NINE"
website: www.korveltnine.com.au (under construction)

Offices: *Perth *Brisbane *Seoul *Hong Kong

If you need any further information please let me know!

Cheers

Lionel

```html
<!DOCTYPE html>
<html lang="en">
<head>
<meta charset="utf-8">
<title>KORVELT-NINE Letterhead Options</title>
<link href="https://fonts.googleapis.com/css2?family=Exo+2:wght@200&family=Open+Sans:wght@400&family=Tinos&display=swap" rel="stylesheet">
<style>
  :root {
    --backdrop: #8b5a33;
    --paper: #ffffff;
    --ink: #3a3a3a;
    --brand-blue: #1e96dc;
    --rule: #9aa0a6;
    --label: #ffffff;
  }
  * { margin: 0; padding: 0; box-sizing: border-box; }
  html, body { width: 1200px; height: 887px; overflow: hidden; }
  body { background: var(--backdrop); position: relative; font-family: "Tinos", serif; }

  .sheet {
    position: absolute; top: 36px; width: 546px; height: 774px;
    background: var(--paper);
    box-shadow: 0 2px 6px rgba(0,0,0,0.35);
    overflow: hidden;
  }
  .sheet--centered { left: 45px; }
  .sheet--banded { left: 622px; }

  .brand { position: absolute; top: 18px; display: flex; align-items: center; gap: 16px; }
  .sheet--centered .brand { left: 132px; }
  .sheet--banded .brand { left: 15px; }
  .brand__mark { width: 96px; height: 96px; background: var(--brand-blue); }
  .brand__name {
    font-family: "Exo 2", sans-serif; font-weight: 200;
    font-size: 28px; letter-spacing: 1px; color: var(--ink); line-height: 1;
  }

  .contact-line { display: inline-flex; align-items: center; gap: 4px; white-space: nowrap; }
  .icon { width: 10px; height: 10px; flex: none; }

  .footer-centered {
    position: absolute; left: 0; right: 0; top: 728px;
    text-align: center; font-size: 12.5px; line-height: 16px; color: var(--ink);
  }
  .footer-centered .address { display: block; }
  .footer-centered .contacts { display: flex; justify-content: center; gap: 8px; margin-top: 4px; }

  .contact-block {
    position: absolute; left: 387px; top: 33px; height: 54px;
    border-left: 1px solid var(--rule); padding-left: 9px;
    display: flex; flex-direction: column; justify-content: space-between;
    font-size: 12.5px; font-style: normal; color: var(--ink); padding-top: 3px;
  }

  .footer-band {
    position: absolute; left: 0; right: 0; bottom: 0; height: 21px;
    background: var(--brand-blue);
    border-top: 3px solid var(--paper);
    box-shadow: 0 -1px 0 var(--rule);
    color: #ffffff; font-size: 12.5px; text-align: center; line-height: 18px;
  }

  .option-label {
    position: absolute; top: 820px; width: 300px; text-align: center;
    font-family: "Open Sans", sans-serif; font-size: 41px; line-height: 50px; color: var(--label);
  }
  .option-label--one { left: 195px; }
  .option-label--two { left: 748px; }
</style>
</head>
<body>
<svg width="0" height="0" style="position:absolute" aria-hidden="true">
  <defs>
    <symbol id="icon-phone" viewBox="0 0 10 10">
      <circle cx="5" cy="5" r="4.3" fill="none" stroke="#2a5d9a" stroke-width="1"/>
      <path d="M3.4 3 L4.3 2.8 L4.6 4 L4 4.4 Q4.6 5.6 5.6 6 L6 5.4 L7.2 5.7 L7 6.6 Q4 6.8 3.4 3 Z" fill="#2a5d9a"/>
    </symbol>
    <symbol id="icon-mail" viewBox="0 0 10 10">
      <rect x="1" y="2.5" width="8" height="5.5" rx="0.6" fill="#2a5d9a"/>
      <path d="M1.4 3 L5 5.8 L8.6 3" fill="none" stroke="#ffffff" stroke-width="0.8"/>
    </symbol>
    <symbol id="icon-web" viewBox="0 0 10 10">
      <circle cx="5" cy="5" r="4" fill="#5d7ea8"/>
      <path d="M1 5 H9 M5 1 V9 M2 3 H8 M2 7 H8" stroke="#ffffff" stroke-width="0.5" fill="none"/>
      <ellipse cx="5" cy="5" rx="1.8" ry="4" fill="none" stroke="#ffffff" stroke-width="0.5"/>
    </symbol>
  </defs>
</svg>

<section class="sheet sheet--centered" aria-label="Letterhead option one">
  <header class="brand">
    <div class="brand__mark"></div>
    <span class="brand__name">korvelt-nine</span>
  </header>
  <footer class="footer-centered">
    <span class="address">00, Complex Name, City, State 0004</span>
    <div class="contacts">
      <span class="contact-line"><svg class="icon"><use href="#icon-phone"/></svg>123-456-7890</span>
      <span class="contact-line"><svg class="icon"><use href="#icon-mail"/></svg>info@korveltnine.com.au</span>
      <span class="contact-line"><svg class="icon"><use href="#icon-web"/></svg>www.korveltnine.com.au</span>
    </div>
  </footer>
</section>

<section class="sheet sheet--banded" aria-label="Letterhead option two">
  <header class="brand">
    <div class="brand__mark"></div>
    <span class="brand__name">korvelt-nine</span>
  </header>
  <address class="contact-block">
    <span class="contact-line"><svg class="icon"><use href="#icon-phone"/></svg>123-456-7890</span>
    <span class="contact-line"><svg class="icon"><use href="#icon-mail"/></svg>info@korveltnine.com.au</span>
    <span class="contact-line"><svg class="icon"><use href="#icon-web"/></svg>www.korveltnine.com.au</span>
  </address>
  <footer class="footer-band">00, Complex Name, City, State 0004</footer>
</section>

<p class="option-label option-label--one">Option-1</p>
<p class="option-label option-label--two">Option-2</p>
</body>
</html>
```